7 variations of an already existing packet design needed

i need 8 colour and flavour variations of a design that i have already in AI/PDF/PSD format

i need 7 colour variations of the packet with the names of the flavours incorporated onto the packaging itself.

the 7 colour/flavour variations i want are

pineapple
cherry
blueberry
bubblegum
strawberry
menthol
mango
Apple & Blackcurrant

Requirements
Must have
• Must use the original design and have different colour anf flavour variations as described in the brief.
Should not have
• Not be an original design

```html
<!DOCTYPE html>
<html lang="en">
<head>
<meta charset="utf-8">
<title>Regal Haze – Flavour Range Pack Lids</title>
<link href="https://fonts.googleapis.com/css2?family=Bodoni+Moda:wght@500&display=swap" rel="stylesheet">
<style>
  :root {
    --stage: #111112;
    --lid: #1b1b1c;
    --lid-edge: #262627;
    --brand: #e9d9a6;
    --pineapple: #e0a81e;
    --cherry: #d01f3c;
    --blueberry: #4a76e0;
    --bubblegum: #ff72b8;
    --strawberry: #ef4257;
    --menthol: #52d6c8;
    --mango: #ff9c22;
    --apple-blackcurrant: #9b4fd0;
  }
  html, body {
    margin: 0;
    padding: 0;
    width: 1200px;
    height: 846px;
    overflow: hidden;
    background: var(--stage);
  }
  .range {
    box-sizing: border-box;
    width: 1200px;
    height: 846px;
    padding: 16px;
    display: grid;
    grid-template-columns: repeat(4, 1fr);
    grid-template-rows: repeat(2, 1fr);
    gap: 16px;
  }
  .lid {
    position: relative;
    background: var(--lid);
    box-shadow: inset 0 0 0 6px var(--lid-edge);
    overflow: hidden;
  }
  .lid--pineapple { --flavour: var(--pineapple); }
  .lid--cherry { --flavour: var(--cherry); }
  .lid--blueberry { --flavour: var(--blueberry); }
  .lid--bubblegum { --flavour: var(--bubblegum); }
  .lid--strawberry { --flavour: var(--strawberry); }
  .lid--menthol { --flavour: var(--menthol); }
  .lid--mango { --flavour: var(--mango); }
  .lid--apple-blackcurrant { --flavour: var(--apple-blackcurrant); }

  .smoke {
    position: absolute;
    width: 34px;
    height: 250px;
    border-radius: 20px;
    background: linear-gradient(to top, var(--flavour), transparent);
    opacity: 0.75;
    filter: blur(9px);
  }
  .smoke--left {
    left: 70px;
    top: 70px;
    transform: rotate(32deg);
  }
  .smoke--right {
    right: 50px;
    top: 170px;
    transform: rotate(40deg);
  }
  .brand {
    position: absolute;
    left: 0;
    right: 0;
    top: 58px;
    display: flex;
    flex-direction: column;
    align-items: center;
    gap: 12px;
  }
  .brand-dot {
    width: 26px;
    height: 26px;
    border-radius: 50%;
    background: var(--brand);
  }
  .brand-name {
    margin: 0;
    font-family: "Bodoni Moda", serif;
    font-weight: 500;
    font-size: 26px;
    letter-spacing: 2px;
    color: var(--brand);
    white-space: nowrap;
  }
  .flavour {
    position: absolute;
    left: 20px;
    right: 20px;
    top: 210px;
    margin: 0;
    font-family: "Bodoni Moda", serif;
    font-weight: 500;
    font-size: 34px;
    line-height: 1.15;
    letter-spacing: 1px;
    text-align: center;
    color: var(--flavour);
  }
</style>
</head>
<body>
  <main class="range">
    <section class="lid lid--pineapple">
      <div class="smoke smoke--left" role="img" aria-label="Wisp of pineapple-gold smoke"></div>
      <div class="smoke smoke--right" role="img" aria-label="Wisp of pineapple-gold smoke"></div>
      <div class="brand"><span class="brand-dot"></span><p class="brand-name">Regal Haze</p></div>
      <h2 class="flavour">Pineapple</h2>
    </section>
    <section class="lid lid--cherry">
      <div class="smoke smoke--left" role="img" aria-label="Wisp of cherry-red smoke"></div>
      <div class="smoke smoke--right" role="img" aria-label="Wisp of cherry-red smoke"></div>
      <div class="brand"><span class="brand-dot"></span><p class="brand-name">Regal Haze</p></div>
      <h2 class="flavour">Cherry</h2>
    </section>
    <section class="lid lid--blueberry">
      <div class="smoke smoke--left" role="img" aria-label="Wisp of blueberry-blue smoke"></div>
      <div class="smoke smoke--right" role="img" aria-label="Wisp of blueberry-blue smoke"></div>
      <div class="brand"><span class="brand-dot"></span><p class="brand-name">Regal Haze</p></div>
      <h2 class="flavour">Blueberry</h2>
    </section>
    <section class="lid lid--bubblegum">
      <div class="smoke smoke--left" role="img" aria-label="Wisp of bubblegum-pink smoke"></div>
      <div class="smoke smoke--right" role="img" aria-label="Wisp of bubblegum-pink smoke"></div>
      <div class="brand"><span class="brand-dot"></span><p class="brand-name">Regal Haze</p></div>
      <h2 class="flavour">Bubblegum</h2>
    </section>
    <section class="lid lid--strawberry">
      <div class="smoke smoke--left" role="img" aria-label="Wisp of strawberry-red smoke"></div>
      <div class="smoke smoke--right" role="img" aria-label="Wisp of strawberry-red smoke"></div>
      <div class="brand"><span class="brand-dot"></span><p class="brand-name">Regal Haze</p></div>
      <h2 class="flavour">Strawberry</h2>
    </section>
    <section class="lid lid--menthol">
      <div class="smoke smoke--left" role="img" aria-label="Wisp of menthol-mint smoke"></div>
      <div class="smoke smoke--right" role="img" aria-label="Wisp of menthol-mint smoke"></div>
      <div class="brand"><span class="brand-dot"></span><p class="brand-name">Regal Haze</p></div>
      <h2 class="flavour">Menthol</h2>
    </section>
    <section class="lid lid--mango">
      <div class="smoke smoke--left" role="img" aria-label="Wisp of mango-orange smoke"></div>
      <div class="smoke smoke--right" role="img" aria-label="Wisp of mango-orange smoke"></div>
      <div class="brand"><span class="brand-dot"></span><p class="brand-name">Regal Haze</p></div>
      <h2 class="flavour">Mango</h2>
    </section>
    <section class="lid lid--apple-blackcurrant">
      <div class="smoke smoke--left" role="img" aria-label="Wisp of blackcurrant-purple smoke"></div>
      <div class="smoke smoke--right" role="img" aria-label="Wisp of blackcurrant-purple smoke"></div>
      <div class="brand"><span class="brand-dot"></span><p class="brand-name">Regal Haze</p></div>
      <h2 class="flavour">Apple &amp; Blackcurrant</h2>
    </section>
  </main>
</body>
</html>
```